Wordpress Design Papa Academy Project

Need a homepage design for a wordpress site that is based around becoming a better Dad. The sitemap file and logo file are attached. Navigation should be a combination of horizontal and vertical because the sitemap is extensive. I think the Father's conference, Daddy daughter dance and Essay contest would like nice if they were highlighted in their own rounded boxes at the bottom of the home page perhaps. New design needs to be attention grabbing, colorful but not over the top or too flashy either. I would like the background to be pictures and/or transparent words(similar to this site http://kinhearth.com/). Need a banner image which will be a slider and I need text overlay at the bottom of each image. I like rounded boxes like how this site showcases the news and events sections - http://www.qz.edu/. Need to also incorporate an events calendar, facebook and twitter icons and contact info. A preliminary design was initially created and is attached for you to review. Design needs to be balanced as there is alot of info to display.I have a current site here http://www.papaacad.com/ and you will see why I need a new design.
Updates

Reason: Still seeking creative concepts.

Reason: Still finalizing the design.

Target Market(s)

Dads

Industry/Entity Type

Events

Requirements
Must have
• image slider with text overlay on image, combination of horizontal and vertical navigation, show a dropdown menu under one of the horizontal tabs, events calendar, web safe fonts, colorful, use stock images for any placeholders,footer with sitemap
Nice to have
• rounded boxes, highlight father's conference,daddy daughter dance and essay contest in a separate section from the navigation, also put campus book store and online classes in a vertical nav bar perhaps - maybe in bigger placeholders like stacked boxes or similar.

```html
<!DOCTYPE html>
<html lang="en">
<head>
<meta charset="utf-8">
<title>Papa Academy, Inc. — Home</title>
<link rel="stylesheet" href="https://fonts.googleapis.com/css2?family=Arimo:wght@400;700&family=Tinos:wght@400&display=swap">
<style>
:root{
  --header-bg:#fdf0ee;
  --nav-blue:#4d82b8;
  --nav-line:#e08a6a;
  --navy:#1d3f6e;
  --deep-navy:#173563;
  --hero-bg:#a8c0dc;
  --orange:#e8563a;
  --orange-dark:#c7402a;
  --peach:#e3bfa9;
  --box-blue:#4f7fb8;
  --text:#1f3760;
  --white:#fff;
  --menu-gray:#d9d9d9;
  --footer-top:#4f7fb7;
  --footer-bottom:#84a8d2;
}
*{box-sizing:border-box;margin:0;padding:0}
html,body{width:820px;height:1200px;overflow:hidden}
body{position:relative;background:var(--white);font-family:"Arimo",Arial,sans-serif;color:var(--text)}
a{color:inherit;text-decoration:none}
.abs{position:absolute}

/* header */
.site-header{left:0;top:0;width:820px;height:120px;background:var(--header-bg)}
.account-links{right:105px;top:10px;font-size:9px;color:#444;letter-spacing:.3px}
.account-links a{margin-left:12px}
.brand{left:108px;top:36px;display:flex;align-items:center;gap:12px}
.brand-dot{width:44px;height:44px;border-radius:50%;background:var(--navy)}
.brand-name{font-family:"Tinos","Times New Roman",serif;font-size:25px;color:var(--deep-navy)}
.quick-links{left:514px;top:32px;width:202px;height:24px;display:flex;border-radius:6px;overflow:hidden;background:var(--orange);box-shadow:0 1px 2px rgba(0,0,0,.3)}
.quick-links a{flex:auto;white-space:nowrap;color:var(--white);font-size:8px;display:flex;align-items:center;justify-content:center;text-transform:uppercase;padding:0 6px}
.quick-links a+a{border-left:1px solid var(--orange-dark)}
.search{left:636px;top:67px;width:80px;height:13px;display:flex;align-items:center}
.search-field{flex:1;height:12px;border:1px solid #999;border-radius:7px;background:var(--white);font-size:6px;color:#999;padding-left:6px;line-height:10px}
.search-go{width:16px;height:13px;border-radius:7px;background:#4c5866;color:var(--white);font-size:6px;margin-left:-6px;text-align:center;line-height:13px;font-weight:700}
.feature-tabs{left:432px;top:98px;display:flex;gap:3px}
.feature-tabs a{height:22px;border-radius:6px 6px 0 0;color:var(--white);font-size:9px;display:flex;align-items:center;justify-content:center;white-space:nowrap}
.tab-blue{background:var(--navy)}
.tab-peach{background:#eaa896}

/* nav */
.main-nav{left:0;top:120px;width:820px;height:36px;background:var(--nav-blue);border-top:2px solid var(--nav-line);border-bottom:2px solid var(--nav-line)}
.main-nav a{position:absolute;top:9px;font-size:9.5px;color:var(--white)}
.main-nav .current{background:var(--deep-navy);padding:4px 9px;border-radius:4px;top:5px;font-weight:700}

/* hero */
.hero{left:0;top:158px;width:820px;height:382px;background:var(--hero-bg)}
.hero-photo{left:112px;top:166px;width:604px;height:340px;border-radius:4px;background:linear-gradient(110deg,#6b4c3d 0%,#a98069 40%,#d0ab94 60%,#caa58d 100%)}
.hero-caption{left:112px;top:438px;width:604px;height:68px;background:rgba(230,224,232,.85);border-radius:0 0 4px 4px}
.hero-title{left:145px;top:450px;font-size:20px;font-weight:400;color:var(--deep-navy)}
.hero-text{left:145px;top:476px;font-size:12px;color:var(--deep-navy)}
.btn-more{display:flex;align-items:center;justify-content:center;color:var(--white);border-radius:6px}
.hero-more{left:590px;top:457px;width:86px;height:29px;background:var(--orange);font-size:12px;border:1px solid var(--orange-dark)}
.slider-dots{left:387px;top:519px;display:flex;gap:3px}
.slider-dots span{width:7px;height:7px;border-radius:50%;background:var(--box-blue)}
.slider-dots span:first-child{background:#e8998a}

/* dropdown */
.menu-primary{left:368px;top:156px;width:122px;height:222px;background:var(--menu-gray);border-radius:0 0 6px 6px;box-shadow:0 2px 4px rgba(0,0,0,.3);padding-top:6px}
.menu-primary a{display:block;height:24px;line-height:24px;padding-left:23px;font-size:7.5px;color:var(--deep-navy);white-space:nowrap}
.menu-primary a.active{background:#c5c5c5}
.menu-secondary{left:486px;top:156px;width:116px;height:166px;background:var(--deep-navy);border-radius:0 0 6px 6px;box-shadow:0 2px 4px rgba(0,0,0,.3);padding-top:12px}
.menu-secondary a{display:block;height:24px;line-height:24px;padding-left:26px;font-size:7.5px;color:var(--white)}

/* info boxes */
.info-box{top:571px;width:194px;height:189px;border:2px solid var(--box-blue);border-radius:8px;overflow:hidden;background:var(--white)}
.info-head{height:42px;background:var(--peach);display:flex;align-items:center;padding-left:18px;font-size:19px;font-weight:400;color:var(--deep-navy)}
.about-thumb{position:absolute;left:12px;top:52px;width:64px;height:60px;border:1px solid var(--box-blue);display:flex;align-items:center;justify-content:center}
.about-thumb span{width:34px;height:34px;border-radius:50%;background:var(--navy)}
.small-text{font-size:7.5px;line-height:11px;color:var(--text)}
.about-side{position:absolute;left:86px;top:52px;width:100px}
.about-body{position:absolute;left:12px;top:118px;width:175px}
.event-dots{position:absolute;right:12px;top:16px;display:flex;gap:4px}
.event-dots span{width:12px;height:12px;border-radius:50%;border:1px solid #999;background:#e8e8e8}
.event-dots span:first-child{background:#8fa9d0;border-color:#6d8bb8}
.event-row{position:absolute;left:16px;display:flex;align-items:center;gap:15px}
.event-date{width:40px;height:36px;border-radius:6px;background:var(--deep-navy);border:2px solid #c8ad9e;color:var(--white);text-align:center;font-size:11px;line-height:14px;padding-top:3px}
.event-date small{display:block;font-size:8px}
.event-text{width:106px}
.view-all{position:absolute;right:18px;bottom:6px;font-size:7.5px}
.shop-box{border-color:var(--deep-navy)}
.shop-head{position:absolute;left:16px;top:8px;display:flex;align-items:center;gap:36px;font-size:19px;font-weight:400;color:var(--deep-navy)}
.shop-head span{width:34px;height:34px;border-radius:50%;background:var(--navy)}
.shop-item{position:absolute;left:48px;top:50px;width:92px;height:74px;border:1px solid #99b;display:flex;align-items:center;justify-content:center}
.shop-item div{width:40px;height:60px;background:linear-gradient(#7a2a40,#4e1426);border-radius:6px}
.shop-desc{position:absolute;left:50px;top:128px;width:100px}
.shop-price{position:absolute;left:118px;top:151px;font-size:11px}
.shop-buy{position:absolute;left:96px;top:168px;width:42px;height:15px;background:var(--deep-navy);font-size:9px;border-radius:7px}
.shop-arrow{left:694px;top:648px}

/* feature cards */
.feature-card{top:788px;width:194px;height:258px;border:2px solid #edc9b6;border-radius:8px;overflow:hidden;background:var(--white)}
.card-head{height:44px;background:var(--peach);position:relative}
.card-title{position:absolute;right:24px;top:16px;font-size:9px;font-weight:400;color:var(--deep-navy)}
.card-photo{height:120px}
.card-text{position:absolute;left:15px;top:178px;width:165px;font-size:9.5px;line-height:12.5px;color:var(--deep-navy)}
.card-more{position:absolute;right:8px;top:222px;width:62px;height:24px;background:var(--box-blue);font-size:10px;border-radius:6px}
.conf-badge{left:106px;top:778px;width:64px;height:64px;border-radius:50%;background:#c8d6ea;border:3px solid #edc9b6;display:flex;align-items:center;justify-content:center}
.conf-badge span{width:36px;height:36px;border-radius:50%;background:var(--navy)}

/* footer */
.site-footer{left:0;top:1076px;width:820px;height:124px;background:linear-gradient(var(--footer-top),var(--footer-bottom))}
.footer-col{font-size:7.5px;line-height:11px;color:var(--white)}
.footer-col a{display:block}
.footer-org{font-weight:700;font-size:9px;line-height:13px}
.social{display:flex;gap:4px;margin-top:5px}
.social span{width:12px;height:12px;border-radius:2px;background:#dfe7f2}
.footer-mark{left:377px;top:1066px;width:66px;height:66px;border-radius:50%;background:var(--navy);border:3px solid #cfd7e4}
</style>
</head>
<body>

<header class="site-header abs">
  <nav class="account-links abs"><a href="#">LOGIN</a><a href="#">SIGN UP</a></nav>
  <a class="brand abs" href="#"><span class="brand-dot"></span><span class="brand-name">Papa Academy, Inc.</span></a>
  <nav class="quick-links abs"><a href="#">On line classes</a><a href="#">Campus bookstore</a></nav>
  <div class="search abs"><div class="search-field">search</div><div class="search-go">GO</div></div>
  <nav class="feature-tabs abs">
    <a class="tab-blue" href="#" style="width:96px">father's conference</a>
    <a class="tab-peach" href="#" style="width:102px">daddy daughter dance</a>
    <a class="tab-blue" href="#" style="width:80px">essay contest</a>
  </nav>
</header>

<nav class="main-nav abs">
  <a class="current" href="#" style="left:129px">Home</a>
  <a href="#" style="left:202px">About</a>
  <a href="#" style="left:271px">Contact</a>
  <a href="#" style="left:351px">Admissions</a>
  <a href="#" style="left:440px">Information</a>
  <a href="#" style="left:527px">Services</a>
  <a href="#" style="left:601px">Products</a>
  <a href="#" style="left:681px">Blog</a>
</nav>

<section class="hero abs"></section>
<div class="hero-photo abs" role="img" aria-label="Close-up photo of a father and son touching foreheads"></div>
<div class="hero-caption abs"></div>
<h1 class="hero-title abs">Jujubes jelly beans pastry</h1>
<p class="hero-text abs">cake biscuit jujubes oat cake. Candy canes candy canes topping lemon...</p>
<a class="hero-more btn-more abs" href="#">more &gt;&gt;</a>
<div class="slider-dots abs"><span></span><span></span><span></span><span></span></div>

<nav class="menu-primary abs">
  <a class="active" href="#">Education center</a>
  <a href="#">Parenting Classes</a>
  <a href="#">Online parenting classes</a>
  <a href="#">Divorced Dads</a>
  <a href="#">Single Dads</a>
  <a href="#">News and Announcements</a>
  <a href="#">Library</a>
  <a href="#">Resource Center</a>
  <a href="#">Legal information</a>
</nav>
<nav class="menu-secondary abs">
  <a href="#">Orientation (0 -5)</a>
  <a href="#">Freshman (6 -9)</a>
  <a href="#">Sophomore (10- 13)</a>
  <a href="#">Junior (14 – 17)</a>
  <a href="#">Senior (18 and over)</a>
  <a href="#">Alumni ( Mentors)</a>
</nav>

<section class="info-box abs" style="left:109px">
  <h2 class="info-head">About</h2>
  <div class="about-thumb"><span></span></div>
  <p class="about-side small-text">Jujubes jelly beans pastry cake biscuit jujubes oat cake. Candy canes candy canes topping lemon drops liquorice. Fawork chocolate bar cookie tart powder</p>
  <p class="about-body small-text">Jujubes jelly beans pastry cake biscuit jujubes oat cake. Candy canes candy canes topping lemon drops liquorice. Fawork chocolate bar cookie tart powder tootsie roll macaroon liquorice. Bonbon fruitcake croissant. Danish sugar plum</p>
</section>

<section class="info-box abs" style="left:318px">
  <h2 class="info-head">Events</h2>
  <div class="event-dots"><span></span><span></span><span></span></div>
  <div class="event-row" style="top:50px"><div class="event-date">12<small>DEC</small></div><p class="event-text small-text">Jujubes jelly beans pastry cake biscuit jujubes oat</p></div>
  <div class="event-row" style="top:92px"><div class="event-date">01<small>DEC</small></div><p class="event-text small-text">Jujubes jelly beans pastry cake biscuit jujubes oat</p></div>
  <div class="event-row" style="top:134px"><div class="event-date">25<small>NOV</small></div><p class="event-text small-text">Jujubes jelly beans pastry cake biscuit jujubes oat</p></div>
  <a class="view-all" href="#">View all</a>
</section>

<section class="info-box shop-box abs" style="left:523px">
  <h2 class="shop-head"><span></span>Shop</h2>
  <div class="shop-item" role="img" aria-label="Product photo of a maroon hooded jacket"><div></div></div>
  <p class="shop-desc small-text">Jujubes jelly beans pastry cake biscuit jujubes oat</p>
  <p class="shop-price">25 $</p>
  <a class="shop-buy btn-more" href="#">Buy</a>
</section>
<svg class="shop-arrow abs" width="16" height="32" viewBox="0 0 16 32"><path d="M3 2 L13 16 L3 30" fill="none" stroke="#d6c2b8" stroke-width="3"/></svg>

<section class="feature-card abs" style="left:112px">
  <div class="card-head"><h3 class="card-title">Father's Conference</h3></div>
  <div class="card-photo" role="img" aria-label="Illustration of people working around a giant light bulb" style="background:linear-gradient(#e9eedc,#d6dcc4)"></div>
  <p class="card-text">Jujubes jelly beans pastry cake biscuit jujubes oat cake. Candy canes candy canes topping lemon...</p>
  <a class="card-more btn-more" href="#">more &gt;&gt;</a>
</section>
<div class="conf-badge abs"><span></span></div>

<section class="feature-card abs" style="left:318px">
  <div class="card-head">
    <svg style="position:absolute;left:26px;top:8px" width="30" height="30" viewBox="0 0 30 30"><rect x="3" y="6" width="20" height="20" rx="2" fill="none" stroke="#1d3f6e" stroke-width="3"/><path d="M12 18 L26 4" stroke="#1d3f6e" stroke-width="4"/></svg>
    <h3 class="card-title">My Dad Essay Contest</h3>
  </div>
  <div class="card-photo" role="img" aria-label="Photo of a father hugging his young son outdoors" style="background:linear-gradient(#8d8a80,#5d5a52)"></div>
  <p class="card-text">Jujubes jelly beans pastry cake biscuit jujubes oat cake. Candy canes candy canes topping lemon...</p>
  <a class="card-more btn-more" href="#">more &gt;&gt;</a>
</section>

<section class="feature-card abs" style="left:523px">
  <div class="card-head">
    <svg style="position:absolute;left:26px;top:4px" width="26" height="34" viewBox="0 0 26 34"><ellipse cx="9" cy="10" rx="7" ry="9" fill="#1d3f6e"/><ellipse cx="18" cy="12" rx="6" ry="8" fill="#1d3f6e"/><path d="M9 19 L12 33 M18 20 L12 33" stroke="#1d3f6e" stroke-width="1.5"/></svg>
    <h3 class="card-title">Daddy Daughter Dance</h3>
  </div>
  <div class="card-photo" role="img" aria-label="Photo of a little girl in a red coat sitting in autumn leaves" style="background:linear-gradient(#7a6a4c,#a88e5e)"></div>
  <p class="card-text">Jujubes jelly beans pastry cake biscuit jujubes oat cake. Candy canes candy canes topping lemon...</p>
  <a class="card-more btn-more" href="#">more &gt;&gt;</a>
</section>

<footer class="site-footer abs">
  <nav class="footer-col abs" style="left:114px;top:16px">
    <a href="#">Home</a><a href="#">About</a><a href="#">Contact</a><a href="#">Admissions</a><a href="#">Information</a><a href="#">Services</a><a href="#">Products</a><a href="#">Blog</a>
  </nav>
  <div class="footer-col abs" style="left:211px;top:16px">
    <p class="footer-org">Papa Academy</p>
    <p><b>Adress:</b> Maple Grove Lane 27</p>
    <p><b>Tel.:</b> 55 01234</p>
    <p style="margin-top:14px">Follow PA on:</p>
    <div class="social"><span></span><span></span><span></span><span></span><span></span></div>
  </div>
  <nav class="footer-col abs" style="left:502px;top:16px">
    <a href="#">On line Courses</a><a href="#">Campus Bookstore</a>
    <a href="#" style="margin-top:16px">Father's Conference</a><a href="#">Essay Contest</a><a href="#">Daddy Daughter Dance</a>
  </nav>
  <nav class="footer-col abs" style="left:632px;top:16px">
    <a href="#">Father's Conference</a><a href="#">Essay Contest</a><a href="#">Daddy Daughter Dance</a>
    <a href="#">Father's Conference</a><a href="#">Essay Contest</a><a href="#">Daddy Daughter Dance</a>
  </nav>
</footer>
<div class="footer-mark abs"></div>

</body>
</html>
```